PixelGuild CEO Needs a Graphic for a Blog About Crowdsourcing and Online Employment

We need a simple graphic / banner for a blog post that's going to be posted on a large publication (like ByteHerald, Marlowe Commerce Quarterly).

The article will be written by Bram Ostiver (PixelGuild's CEO) and the title will be "Why Websites Will Become the Biggest Employers in the World". The article is about why online employers (like PixelGuild and Tasklynx) will one day have more 'workers' than offline employers.

We'd really like to get this ASAP - so early submissions encouraged. We will try and get the winning designer linked to from the article.

Note that this brief is similar to a previous project that we ran http://jobs.pixelguild-example.com/job.aspx?id=58213 where the article and design was published on ByteHerald http://byteherald-example.com/2012/12/08/asias-hidden-gig-surge/ and the designer (Moravia) was linked to from ByteHerald.

Target Market(s)

Entrepreneurs, journalists, small business owners, tech people.

Industry/Entity Type

Business

Requirements
Must have
• The graphic SHOULD have:
1) Have the text "Why Websites Will Become the Biggest Employers in the World" with some nice design and fonts (consider grey subtle pattern background and white drop shadow on fonts) - see attached examples
2) Have the dimensions 640px wide by 240px wide
Nice to have
• The graphic COULD have:

1) Incorporate the following words in the background (like a word cloud): crowdsource, microtask, crowdfund, witkey, outsource, freelance, online, work from home

OR

2) Incorporate logos of new online employers (Tasklynx, vYard, PixelGuild, ChoreFinch, Lunqiaofu, ClockworkPawn, Frameharbor) into the design. If the background of the graphic is grey, ideally, these logos would also be greyscale i.e. they should form a background motif.

OR

3) Show some graphic communicating themes from the article e.g. laptop, globe, workers, connections across the globe

OR

4) Have a second line of text "Why Crowdsourcing Websites Will Overtake Traditional Employers"
Should not have
• Should NOT have:
1) Any photos or clipart

```html
<!DOCTYPE html>
<html lang="en">
<head>
<meta charset="utf-8">
<title>Why Websites Will Become the Biggest Employers in the World?</title>
<link rel="stylesheet" href="https://fonts.googleapis.com/css2?family=Alfa+Slab+One&family=Oswald:wght@400;500&display=swap">
<style>
  :root {
    --bg: #f1f1f1;
    --bg-line: rgba(0, 0, 0, 0.025);
    --blue: #1b9ad8;
    --ink: #2f2f2f;
    --highlight: #ffffff;
    --art-light: #fbfbfb;
    --art-mid: #e4e4e4;
  }
  * { box-sizing: border-box; margin: 0; padding: 0; }
  html, body {
    width: 1200px;
    height: 450px;
    overflow: hidden;
  }
  .banner {
    position: relative;
    width: 1200px;
    height: 450px;
    background-color: var(--bg);
    background-image:
      repeating-linear-gradient(45deg, var(--bg-line) 0 1px, transparent 1px 6px),
      repeating-linear-gradient(-45deg, var(--bg-line) 0 1px, transparent 1px 6px);
    overflow: hidden;
  }
  .headline {
    position: absolute;
    left: 0;
    top: 0;
    width: 660px;
    height: 450px;
    font-weight: normal;
  }
  .headline svg {
    display: block;
    width: 660px;
    height: 450px;
    overflow: visible;
  }
  .initial {
    font-family: "Alfa Slab One", serif;
    font-size: 215px;
    fill: var(--blue);
    filter: drop-shadow(0 2px 0 var(--highlight));
  }
  .keyword {
    font-family: "Oswald", sans-serif;
    font-weight: 500;
    font-size: 54px;
    fill: var(--blue);
    filter: drop-shadow(0 2px 0 var(--highlight));
  }
  .headline-rest {
    font-family: "Oswald", sans-serif;
    font-weight: 400;
    font-size: 56px;
    fill: var(--ink);
    filter: drop-shadow(0 2px 0 var(--highlight));
  }
  .artwork {
    position: absolute;
    left: 700px;
    top: 84px;
    width: 400px;
    height: 246px;
    border-radius: 30px;
    background: radial-gradient(ellipse at 50% 50%, var(--art-light) 0%, var(--art-mid) 55%, var(--bg) 100%);
  }
</style>
</head>
<body>
  <main class="banner">
    <h1 class="headline">
      <svg viewBox="0 0 660 450" aria-label="Why Websites Will Become the Biggest Employers in the World?">
        <g aria-hidden="true">
          <text class="initial" x="38" y="173" textLength="172" lengthAdjust="spacingAndGlyphs">W</text>
          <text class="initial" x="221" y="173" textLength="167" lengthAdjust="spacingAndGlyphs">W</text>
          <text class="initial" x="424" y="173" textLength="161" lengthAdjust="spacingAndGlyphs">W</text>
        </g>
        <text class="keyword" x="75" y="225" textLength="122" lengthAdjust="spacingAndGlyphs">WHY</text>
        <text class="keyword" x="221" y="225" textLength="167" lengthAdjust="spacingAndGlyphs">WEBSITES</text>
        <text class="keyword" x="435" y="225" textLength="122" lengthAdjust="spacingAndGlyphs">WILL</text>
        <text class="headline-rest" x="75" y="306" textLength="388" lengthAdjust="spacingAndGlyphs">BECOME THE BIGGEST</text>
        <text class="headline-rest" x="75" y="377" textLength="501" lengthAdjust="spacingAndGlyphs">EMPLOYERS IN THE WORLD ?</text>
      </svg>
    </h1>
    <div class="artwork" role="img" aria-label="Illustration of a white desktop computer showing a world map, beside a large silver dollar sign"></div>
  </main>
</body>
</html>
```